11 x 17 Orvanthes Quote

Design the following quote in a poster.

"First say to yourself what you would be; then do what you have to do." - Orvanthes

See here for inspiration - https://prints.mornbrekal.com/

Quote

```html
<!DOCTYPE html>
<html lang="en">
<head>
<meta charset="UTF-8">
<title>Orvanthes Quote Poster</title>
<link rel="stylesheet" href="https://fonts.googleapis.com/css2?family=Cabin+Sketch:wght@400&family=Cabin:wght@500&display=swap">
<style>
  :root {
    --backdrop: #e9e6df;
    --paper: #f7f4e9;
    --ink: #3b3a38;
    --accent: #d2411f;
    --branch-tint: #dfe9e0;
  }
  html, body {
    margin: 0;
    padding: 0;
    width: 1200px;
    height: 750px;
    overflow: hidden;
    background: var(--backdrop);
  }
  .poster {
    position: absolute;
    left: 400px;
    top: 62px;
    width: 414px;
    height: 626px;
    background: var(--paper);
    box-shadow: 0 2px 10px rgba(0,0,0,0.12);
    overflow: hidden;
  }
  .blossom-branch {
    position: absolute;
    left: 30px;
    top: 480px;
    width: 384px;
    height: 146px;
    background: linear-gradient(160deg, rgba(247,244,233,0) 10%, var(--branch-tint) 50%, rgba(247,244,233,0) 90%);
    opacity: 0.55;
  }
  .quote {
    position: absolute;
    inset: 0;
    margin: 0;
    font-family: "Cabin Sketch", cursive;
    font-weight: 400;
    color: var(--ink);
    text-align: center;
    font-size: 40px;
    letter-spacing: 1px;
  }
  .quote .line {
    position: absolute;
    left: 0;
    width: 100%;
    line-height: 1;
  }
  .quote .accent {
    color: var(--accent);
    font-size: 42px;
  }
  .attribution {
    position: absolute;
    left: 0;
    width: 100%;
    top: 592px;
    margin: 0;
    line-height: 1;
    text-align: center;
    font-family: "Cabin", sans-serif;
    font-weight: 500;
    font-size: 19px;
    letter-spacing: 1px;
    color: var(--ink);
  }
</style>
</head>
<body>
  <main class="poster">
    <div class="blossom-branch" role="img" aria-label="Faint painted branch of white blossoms"></div>
    <blockquote class="quote">
      <span class="line" style="top:32px">“First say to</span>
      <span class="line" style="top:86px">yourself</span>
      <span class="line" style="top:144px">what you</span>
      <span class="line accent" style="top:204px">would be</span>
      <span class="line" style="top:330px">then do what</span>
      <span class="line" style="top:386px">you have</span>
      <span class="line accent" style="top:444px">to do”</span>
    </blockquote>
    <p class="attribution">Orvanthes</p>
  </main>
</body>
</html>
```